Homepage design for female-owned English/French speaking Law firm

Brief Update - we prefer not to have a photo of a person in the hero shot

Corvell.com.au is the website for a English/French Bilingual Female-owned Law Firm, Morillaqua Corvell.
Overall Design notes:
Professional, yet warm and welcoming
Historic foundations but Progressive, woman-owned, sleek, innovative and modern.
Approachable, casual yet professional. Sans-serif font and light colours would help this
2 languages switched by flags (English/French)

Winner must provide
Home page design
Standard (inner) page design (can be provided after winner is selected)
All photos used in the design without charge
Updates

Requirements
Should not have
• Update - we prefer not to have a photo of a person in the hero shot

```html
<!DOCTYPE html>
<html lang="en">
<head>
<meta charset="utf-8">
<title>Morillaqua Corvell</title>
<link href="https://fonts.googleapis.com/css2?family=Poppins:wght@300;400;500;600&display=swap" rel="stylesheet">
<style>
:root{
  --orange:#f7a24e;
  --ink:#1f1f1f;
  --page:#f5f5f5;
  --card:#f1f1f1;
  --white:#ffffff;
  --footer:#1c1c1c;
  --star:#e8b83a;
}
*{box-sizing:border-box;margin:0;padding:0}
html,body{width:1200px;height:5138px;overflow:hidden}
body{font-family:'Poppins',sans-serif;color:var(--ink);background:var(--page);position:relative}
.abs{position:absolute}
.topbar{left:0;top:0;width:1200px;height:44px;background:var(--orange);color:#fff;font-size:14px}
.topbar span{position:absolute;top:13px}
.nav{left:0;top:44px;width:1200px;height:96px;background:#fff}
.brand{position:absolute;left:14px;top:32px;display:flex;align-items:center;gap:12px}
.brand-mark{width:22px;height:22px;background:var(--orange)}
.brand-name{font-size:24px;font-weight:500;color:var(--ink);line-height:32px}
.menu{position:absolute;top:42px;font-size:15px;font-weight:500}
.btn{display:flex;align-items:center;justify-content:center;font-weight:500;text-transform:uppercase}
.btn-solid{background:var(--orange);color:#fff}
.btn-line{border:2px solid var(--orange);color:var(--orange)}
.hero{left:0;top:140px;width:1200px;height:640px;background:linear-gradient(180deg,#3b4a5e 0%,#6d7f94 45%,#7b8796 70%,#2c3a4a 100%)}
.hero-rule{left:0;top:780px;width:1200px;height:6px;background:var(--orange)}
.hero h1{position:absolute;width:100%;top:156px;text-align:center;font-size:52px;font-weight:500;color:#fff}
.hero p{position:absolute;left:300px;width:600px;top:240px;text-align:center;font-size:17px;line-height:28px;color:#fff}
.dot{position:absolute;top:576px;width:22px;height:22px;border-radius:50%;background:#fff}
.eyebrow{font-size:17px;color:var(--orange);text-transform:uppercase}
.section-title{font-size:36px;font-weight:600}
.center{text-align:center;width:1200px;left:0}
.lead{font-size:15px;line-height:24px;color:#777}
.features{left:106px;top:1460px;width:1000px;height:204px;background:#fff;border-radius:18px}
.feature{position:absolute;top:56px;width:300px}
.feature-icon{position:absolute;left:0;top:0;width:86px;height:86px;border-radius:8px;background:#fbe2c8}
.feature h3{position:absolute;left:106px;top:0;font-size:17px;font-weight:500}
.feature p{position:absolute;left:102px;top:24px;width:200px;font-size:14px;line-height:22px;color:#888}
.service-img{position:absolute;width:284px;height:210px;background:linear-gradient(135deg,#9a8b7c,#4c4540)}
.service-body{position:absolute;width:248px;height:160px;background:#fff;padding:30px 32px}
.service-body h3{font-size:15px;font-weight:500;margin-bottom:10px}
.service-body p{font-size:10px;line-height:16px;color:#888}
.read{font-size:10px;color:var(--orange);text-decoration:underline;margin-top:10px;display:block}
.testi-band{left:0;top:2846px;width:1200px;height:614px;background:#fff}
.testi{position:absolute;top:3136px;width:308px;height:210px;background:var(--card);text-align:center}
.avatar{position:absolute;top:-54px;left:104px;width:100px;height:100px;border-radius:50%;background:linear-gradient(135deg,#d7d7d7,#3a3a3a)}
.stars{position:absolute;top:84px;width:100%;display:flex;justify-content:center}
.testi p{position:absolute;top:122px;left:30px;width:248px;font-size:9.5px;line-height:14px;color:#777}
.testi .who{position:absolute;top:178px;width:100%;font-size:13px;color:var(--orange)}
.blog-img{position:absolute;width:280px;height:146px;background:linear-gradient(135deg,#b8b2a9,#5e574f)}
.blog-body{position:absolute;width:280px;height:128px;background:#fff;padding:18px 16px}
.blog-body h3{font-size:20px;font-weight:500;margin-bottom:6px}
.blog-body p{font-size:9.5px;line-height:15px;color:#888}
.contact{left:0;top:4080px;width:1200px;height:624px;background:linear-gradient(180deg,#f5a65a,#f6b97a 60%,#f5b275)}
.field{position:absolute;background:#fff;font-size:12.5px;font-weight:500;color:#444;padding:20px 24px;text-transform:uppercase}
.footer{left:0;top:4704px;width:1200px;height:434px;background:var(--footer);color:#fff}
.foot-brand{position:absolute;left:36px;top:164px;font-size:18px;font-weight:500;color:#fff}
.foot-h{position:absolute;top:110px;font-size:21px;font-weight:500;color:var(--orange);text-decoration:underline;text-transform:uppercase}
.foot-link{position:absolute;left:362px;font-size:17px}
.foot-info{position:absolute;left:614px;font-size:17px;display:flex;gap:14px;align-items:flex-start;line-height:22px}
.social{position:absolute;top:222px;width:20px;height:20px;border-radius:50%;background:var(--orange)}
.small{font-size:11px;color:#ccc}
</style>
</head>
<body>

<div class="abs topbar">
  <svg class="abs" style="left:34px;top:14px" width="20" height="16" viewBox="0 0 20 16"><rect x="1" y="1" width="18" height="14" rx="1" fill="none" stroke="#fff" stroke-width="2"/><path d="M1 2l9 7 9-7" fill="none" stroke="#fff" stroke-width="2"/></svg>
  <span style="left:74px">nadine@corvell.com.au</span>
  <svg class="abs" style="left:282px;top:14px" width="16" height="16" viewBox="0 0 24 24"><path d="M6.6 10.8a15 15 0 006.6 6.6l2.2-2.2a1 1 0 011-.25 11 11 0 003.5.56 1 1 0 011 1V20a1 1 0 01-1 1A17 17 0 013 4a1 1 0 011-1h3.5a1 1 0 011 1 11 11 0 00.56 3.5 1 1 0 01-.25 1z" fill="#fff"/></svg>
  <span style="left:310px">+612 9000 4120</span>
  <svg class="abs" style="left:1084px;top:6px" width="32" height="32" viewBox="0 0 32 32" role="img" aria-label="English"><circle cx="16" cy="16" r="15" fill="#24407a"/><rect x="12" y="1" width="8" height="30" fill="#fff"/><rect x="1" y="12" width="30" height="8" fill="#fff"/><rect x="14" y="1" width="4" height="30" fill="#c8102e"/><rect x="1" y="14" width="30" height="4" fill="#c8102e"/></svg>
  <svg class="abs" style="left:1130px;top:6px" width="32" height="32" viewBox="0 0 32 32" role="img" aria-label="Français"><defs><clipPath id="fc"><circle cx="16" cy="16" r="15"/></clipPath></defs><g clip-path="url(#fc)"><rect x="0" y="0" width="11" height="32" fill="#1f3f9c"/><rect x="11" y="0" width="10" height="32" fill="#fff"/><rect x="21" y="0" width="11" height="32" fill="#e1262d"/></g></svg>
</div>

<div class="abs nav">
  <div class="brand"><div class="brand-mark"></div><div class="brand-name">Morillaqua Corvell</div></div>
  <div class="menu" style="left:456px">HOME</div>
  <div class="menu" style="left:534px">ABOUT US</div>
  <div class="menu" style="left:648px">SERVICES</div>
  <div class="menu" style="left:756px">DOWNLOAD</div>
  <div class="menu" style="left:886px">BLOG</div>
  <div class="abs btn btn-solid" style="left:1020px;top:32px;width:150px;height:42px;font-size:15px">Contact Us</div>
</div>

<div class="abs hero" role="img" aria-label="Harbour city skyline with waterfront opera house under a cloudy sky">
  <h1>QUALITY LEGAL SERVICES</h1>
  <p>Our small, skilled team is committed to the delivery of quality legal services to our clients.</p>
  <div class="abs btn btn-solid" style="left:516px;top:318px;width:152px;height:42px;font-size:15px">Contact Us</div>
  <div class="dot" style="left:552px"></div>
  <div class="dot" style="left:588px;background:var(--orange)"></div>
  <div class="dot" style="left:624px"></div>
</div>
<div class="abs hero-rule"></div>

<div class="abs" role="img" aria-label="Lawyer presenting documents to clients in an office" style="left:64px;top:906px;width:460px;height:460px;border-radius:50%;background:linear-gradient(135deg,#8c7563,#4a3d35 60%,#a99c90)"></div>
<div class="abs eyebrow" style="left:594px;top:982px">About Us</div>
<div class="abs section-title" style="left:594px;top:1010px;font-size:35px;line-height:46px;width:560px">We Delivery Quality Legal Services to Our Clients.</div>
<p class="abs lead" style="left:594px;top:1126px;width:556px">Lorem ipsum dolor sit amet, consectetur adipiscing elit, sed do eiusmod tempor incididunt ut labore et dolore magna aliqua. Ut enim ad minim veniam, quis nostrud exercitation ullamco laboris nisi ut aliquip ex ea commodo consequat.</p>
<div class="abs btn btn-solid" style="left:594px;top:1256px;width:234px;height:46px;font-size:17px">Mission Statement</div>
<div class="abs btn btn-line" style="left:846px;top:1256px;width:236px;height:46px;font-size:17px">Nadine Corvell</div>

<div class="abs features">
  <div class="feature" style="left:26px"><div class="feature-icon" role="img" aria-label="Professional lawyer icon"></div><h3>PROFESSIONAL</h3><p>Lorem ipsum dolor sit amet, consectetur adipiscing elit, sed do eiusmod</p></div>
  <div class="feature" style="left:352px"><div class="feature-icon" role="img" aria-label="Scales of justice icon"></div><h3>LEGAL EXPERTS</h3><p>Lorem ipsum dolor sit amet, consectetur adipiscing elit, sed do eiusmod</p></div>
  <div class="feature" style="left:676px;top:62px"><div class="feature-icon" role="img" aria-label="Document and pen icon"></div><h3>AFFORDABLE</h3><p>Lorem ipsum dolor sit amet, consectetur adipiscing elit, sed do eiusmod</p></div>
</div>

<div class="abs eyebrow center" style="top:1756px">What We Do</div>
<div class="abs section-title center" style="top:1796px;left:28px">OUR SERVICES</div>

<div class="service-img" style="left:112px;top:1906px" role="img" aria-label="Smiling lawyer in suit"></div>
<div class="service-body" style="left:132px;top:2096px"><h3>Property Law</h3><p>Lorem ipsum dolor sit amet, consectetur adipiscing elit, sed do eiusmod empor incididunt ut labore et dolore magna aliqua.</p><span class="read">READ MORE</span></div>
<div class="service-img" style="left:474px;top:1906px" role="img" aria-label="Lawyer reading documents in office"></div>
<div class="service-body" style="left:494px;top:2096px"><h3>Sales of Business</h3><p>Lorem ipsum dolor sit amet, consectetur adipiscing elit, sed do eiusmod empor incididunt ut labore et dolore magna aliqua.</p><span class="read">READ MORE</span></div>
<div class="service-img" style="left:836px;top:1906px" role="img" aria-label="Client meeting at a desk"></div>
<div class="service-body" style="left:856px;top:2096px"><h3>Wills and Estates</h3><p>Lorem ipsum dolor sit amet, consectetur adipiscing elit, sed do eiusmod empor incididunt ut labore et dolore magna aliqua.</p><span class="read">READ MORE</span></div>

<div class="service-img" style="left:112px;top:2302px" role="img" aria-label="Translator working at a desk"></div>
<div class="service-body" style="left:132px;top:2492px"><h3>Translation</h3><p>Lorem ipsum dolor sit amet, consectetur adipiscing elit, sed do eiusmod empor incididunt ut labore et dolore magna aliqua.</p><span class="read">READ MORE</span></div>
<div class="service-img" style="left:474px;top:2302px" role="img" aria-label="Older clients in conversation"></div>
<div class="service-body" style="left:494px;top:2492px"><h3>Elder Law</h3><p>Lorem ipsum dolor sit amet, consectetur adipiscing elit, sed do eiusmod empor incididunt ut labore et dolore magna aliqua.</p><span class="read">READ MORE</span></div>
<div class="service-img" style="left:836px;top:2302px;background:linear-gradient(135deg,#e8e6e3,#9c9892)" role="img" aria-label="Power of attorney document with pen"></div>
<div class="service-body" style="left:856px;top:2492px"><h3>Powers of Attorney</h3><p>Lorem ipsum dolor sit amet, consectetur adipiscing elit, sed do eiusmod empor incididunt ut labore et dolore magna aliqua.</p><span class="read">READ MORE</span></div>

<div class="abs btn btn-solid" style="left:512px;top:2740px;width:208px;height:46px;font-size:17px">View All Services</div>

<div class="abs testi-band"></div>
<div class="abs eyebrow center" style="top:2940px">Testimonials</div>
<div class="abs section-title center" style="top:2980px;left:12px;font-size:35px">What Client Says</div>

<div class="testi" style="left:74px"><div class="avatar" role="img" aria-label="Client portrait"></div>
  <div class="stars"><svg width="140" height="20" viewBox="0 0 140 20"><g fill="var(--star)"><path id="st" d="M10 0l3 6.5 7 .8-5.2 4.8 1.4 7L10 15.6 3.8 19l1.4-7L0 7.3l7-.8z"/><use href="#st" x="30"/><use href="#st" x="60"/><use href="#st" x="90"/><use href="#st" x="120"/></g></svg></div>
  <p>Lorem ipsum dolor sit amet, consectetur adipiscing elit, sed do eiusmodtempor incididunt ut labore et dolore magna aliqua. Ut enim ad minim</p><div class="who">JOHN DOE</div></div>
<div class="testi" style="left:456px"><div class="avatar" role="img" aria-label="Client portrait"></div>
  <div class="stars"><svg width="140" height="20" viewBox="0 0 140 20"><g fill="var(--star)"><use href="#st"/><use href="#st" x="30"/><use href="#st" x="60"/><use href="#st" x="90"/><use href="#st" x="120"/></g></svg></div>
  <p>Lorem ipsum dolor sit amet, consectetur adipiscing elit, sed do eiusmodtempor incididunt ut labore et dolore magna aliqua. Ut enim ad minim</p><div class="who">JOHN DOE</div></div>
<div class="testi" style="left:836px"><div class="avatar" role="img" aria-label="Client portrait"></div>
  <div class="stars"><svg width="140" height="20" viewBox="0 0 140 20"><g fill="var(--star)"><use href="#st"/><use href="#st" x="30"/><use href="#st" x="60"/><use href="#st" x="90"/><use href="#st" x="120"/></g></svg></div>
  <p>Lorem ipsum dolor sit amet, consectetur adipiscing elit, sed do eiusmodtempor incididunt ut labore et dolore magna aliqua. Ut enim ad minim</p><div class="who">JOHN DOE</div></div>

<div class="abs eyebrow center" style="top:3554px">News &amp; Updates</div>
<div class="abs section-title center" style="top:3584px;left:8px;font-size:35px">Latest From Blog</div>

<div class="blog-img" style="left:102px;top:3686px" role="img" aria-label="Team meeting around a table"></div>
<div class="blog-body" style="left:102px;top:3832px"><h3>Post Title</h3><p>Lorem ipsum dolor sit amet, consectetur adipiscing elit, sed do eiusmodtempor incididunt ut labore et dolore magna aliqua. Ut enim ad minim</p><span class="read" style="margin-top:6px">READ MORE</span></div>
<div class="blog-img" style="left:452px;top:3686px" role="img" aria-label="Colleagues discussing at a desk"></div>
<div class="blog-body" style="left:452px;top:3832px"><h3>Post Title</h3><p>Lorem ipsum dolor sit amet, consectetur adipiscing elit, sed do eiusmodtempor incididunt ut labore et dolore magna aliqua. Ut enim ad minim</p><span class="read" style="margin-top:6px">READ MORE</span></div>
<div class="blog-img" style="left:800px;top:3686px" role="img" aria-label="Lawyer consulting with a client"></div>
<div class="blog-body" style="left:800px;top:3832px"><h3>Post Title</h3><p>Lorem ipsum dolor sit amet, consectetur adipiscing elit, sed do eiusmodtempor incididunt ut labore et dolore magna aliqua. Ut enim ad minim</p><span class="read" style="margin-top:6px">READ MORE</span></div>

<div class="abs contact" role="img" aria-label="Lawyer at desk with gavel, under warm orange overlay">
  <div class="abs center" style="top:70px;font-size:17px;color:#fff">CONTACT US</div>
  <div class="abs center" style="top:100px;left:14px;font-size:35px;font-weight:500;color:#fff">Get in Touch With Us</div>
  <div class="field" style="left:290px;top:202px;width:302px;height:52px">First Name</div>
  <div class="field" style="left:638px;top:202px;width:304px;height:52px">Last Name</div>
  <div class="field" style="left:290px;top:282px;width:302px;height:52px">Email Address</div>
  <div class="field" style="left:638px;top:282px;width:304px;height:52px">Phone Number</div>
  <div class="field" style="left:290px;top:362px;width:652px;height:122px">Additional Message</div>
  <div class="abs btn" style="left:448px;top:512px;width:306px;height:54px;border:2px solid #fff;color:#fff;font-size:20px">Request a Quote</div>
</div>

<div class="abs footer">
  <div class="foot-brand">Morillaqua Corvell</div>
  <div class="social" style="left:34px" role="img" aria-label="Social profile"></div>
  <div class="social" style="left:84px" role="img" aria-label="Social profile"></div>
  <div class="social" style="left:140px" role="img" aria-label="Social profile"></div>

  <div class="foot-h" style="left:360px">Quick Links</div>
  <div class="foot-link" style="top:158px">HOME</div>
  <div class="foot-link" style="top:202px">ABOUT</div>
  <div class="foot-link" style="top:250px">SERVICES</div>
  <div class="foot-link" style="top:300px">CONTACT</div>

  <div class="foot-h" style="left:612px">Contact Info</div>
  <div class="foot-info" style="top:158px"><svg width="18" height="18" viewBox="0 0 24 24"><path d="M6.6 10.8a15 15 0 006.6 6.6l2.2-2.2a1 1 0 011-.25 11 11 0 003.5.56 1 1 0 011 1V20a1 1 0 01-1 1A17 17 0 013 4a1 1 0 011-1h3.5a1 1 0 011 1 11 11 0 00.56 3.5 1 1 0 01-.25 1z" fill="var(--orange)"/></svg>+61 2 9000 5512</div>
  <div class="foot-info" style="top:214px"><svg width="18" height="18" viewBox="0 0 20 16"><rect x="1" y="1" width="18" height="14" rx="1" fill="none" stroke="var(--orange)" stroke-width="2"/><path d="M1 2l9 7 9-7" fill="none" stroke="var(--orange)" stroke-width="2"/></svg>nadine@corvell.com.au</div>
  <div class="foot-info" style="top:268px"><svg width="18" height="22" viewBox="0 0 18 24"><path d="M9 0a9 9 0 019 9c0 6-9 15-9 15S0 15 0 9a9 9 0 019-9z" fill="var(--orange)"/><circle cx="9" cy="9" r="3.5" fill="var(--footer)"/></svg><span>Level 8, 42 Harbour Lane<br>Sydney, NSW 2000<br>Australia</span></div>

  <div class="foot-h" style="left:948px">Newsletter</div>
  <div class="abs" style="left:944px;top:162px;width:196px;height:34px;background:#fff;color:#333;font-size:11px;padding:10px 20px">EMAIL ADDRESS</div>
  <div class="abs btn btn-solid" style="left:944px;top:218px;width:196px;height:34px;font-size:15px">Signup Now</div>

  <div class="abs small" style="left:36px;top:406px">©2017-2022 Law Firm | All rights reserved</div>
  <div class="abs small" style="left:906px;top:406px">Privacy Policy | Term and Conditions</div>
</div>

</body>
</html>
```